Ranked amongst the Best Colleges and Programs

the size of the ad is Full Page, with bleed*
8”x 10.75" plus 0.25" bleed'
you have two choices for the tagline .. please chose what ever you think will allow you to make a better ad.
The instructions on the brief are in red
I am looking for a hight quality modern ad to place in local weekly publications that will stand out .
I would like a ad that people will look at and say i would like to see what this ad is all about.
I apprecate creative work.
the ad should not be very crowded and the text should be able to be read.
if you decide to use people in the ad .. (you don't have to ) then it should be a male dressed in white shirt in and sports jacket.. or if you would like you can use a vector and then use male or female people.
please leave one inch on the bottom for the footer

Target Market(s)

potential middle class students from 23-35 years of age

Industry/Entity Type

education

Requirements
Must have
• .the " 98% employment rate" should stand out in the ad.. but should not be the main part of the ad
Nice to have
• creative
Should not have
• Should not be a very busy or crowded ad.. i prefer pictures of men but should be .. in a business suit .. that looks professional- white shirt

```html
<!DOCTYPE html>
<html lang="en">
<head>
<meta charset="utf-8">
<title>NRU Masters of Accounting</title>
<link rel="stylesheet" href="https://fonts.googleapis.com/css2?family=Fraunces:opsz,wght@144,900&family=Prata&family=Tinos:wght@400;700&family=Open+Sans:wght@400;600;700&display=swap">
<style>
  :root {
    --navy: #272466;
    --teal: #0471a3;
    --white: #ffffff;
    --ink: #111111;
    --frame: #c8c8c8;
    --badge-grey: #d9d9dc;
    --badge-amber: #f8b335;
  }
  * { margin: 0; padding: 0; box-sizing: border-box; }
  html, body { width: 893px; height: 1200px; overflow: hidden; background: var(--white); }
  .ad {
    position: relative;
    width: 893px;
    height: 1200px;
    background: var(--white);
    border: 1px solid var(--frame);
    overflow: hidden;
  }
  .headline { position: absolute; left: 0; top: 0; width: 893px; height: 700px; }
  .serif-line { font-family: "Prata", "Playfair Display", serif; fill: var(--navy); }
  .display-line { font-family: "Fraunces", "Georgia", serif; font-weight: 900; fill: var(--teal); }
  .stat-number { font-family: "Open Sans", sans-serif; font-weight: 700; fill: var(--navy); }
  .stat-percent { font-family: "Open Sans", sans-serif; font-weight: 400; fill: var(--navy); }
  .stat-label { font-family: "Open Sans", sans-serif; font-weight: 400; fill: var(--navy); }
  .stat-rule { stroke: var(--navy); stroke-width: 2.5; stroke-linecap: round; }

  .program-band {
    position: absolute; left: 0; top: 703px; width: 893px; height: 81px;
    background: var(--teal);
    display: flex; align-items: center; justify-content: center;
  }
  .program-title {
    font-family: "Tinos", "Times New Roman", serif;
    font-weight: 700; font-size: 46px; color: var(--white);
    letter-spacing: 0.5px;
  }

  .rankings { position: absolute; left: 0; top: 788px; width: 893px; text-align: center; }
  .rankings-label {
    font-family: "Open Sans", sans-serif; font-weight: 600; font-size: 17px; color: var(--ink);
  }
  .badge { position: absolute; top: 34px; width: 200px; text-align: center; }
  .badge-college { left: 249px; }
  .badge-master { left: 441px; }
  .badge-shape { margin: 0 auto; }
  .badge-college .badge-shape { width: 116px; height: 129px; background: var(--badge-grey); }
  .badge-master .badge-shape { width: 99px; height: 124px; background: var(--badge-amber); }
  .badge-caption {
    font-family: "Open Sans", sans-serif; font-size: 12.5px; line-height: 16px; color: var(--ink);
    margin-top: 10px;
  }
  .badge-master .badge-caption { margin-top: 15px; }

  .outcomes-band {
    position: absolute; left: 0; top: 995px; width: 893px; height: 70px;
    background: var(--teal);
    display: flex; align-items: center; justify-content: center;
  }
  .outcomes-text {
    font-family: "Tinos", "Times New Roman", serif; font-size: 19.5px; line-height: 26px;
    color: var(--white); text-align: center;
  }
</style>
</head>
<body>
<main class="ad">
  <svg class="headline" viewBox="0 0 893 700" xmlns="http://www.w3.org/2000/svg" aria-label="A small investment today, a big difference tomorrow">
    <text class="serif-line" x="186" y="128" font-size="98" textLength="312" lengthAdjust="spacingAndGlyphs">A small</text>
    <text class="display-line" x="143" y="224" font-size="132" textLength="672" lengthAdjust="spacingAndGlyphs">investment</text>
    <text class="serif-line" x="543" y="305" font-size="92" textLength="241" lengthAdjust="spacingAndGlyphs">today,</text>

    <g class="employment-stat" transform="translate(238 413) rotate(-27)">
      <line class="stat-rule" x1="-46" y1="-93" x2="170" y2="-93"/>
      <line class="stat-rule" x1="-42" y1="42" x2="174" y2="42"/>
      <text class="stat-number" x="6" y="-16" font-size="88" textLength="98" lengthAdjust="spacingAndGlyphs">98</text>
      <text class="stat-percent" x="108" y="-52" font-size="30">%</text>
      <text class="stat-label" x="0" y="0" font-size="21" textLength="138" lengthAdjust="spacingAndGlyphs">employment</text>
      <text class="stat-label" x="46" y="27" font-size="21" textLength="44" lengthAdjust="spacingAndGlyphs">rate</text>
    </g>

    <text class="serif-line" x="405" y="511" font-size="110">a</text>
    <text class="display-line" x="481" y="511" font-size="250" textLength="338" lengthAdjust="spacingAndGlyphs">big</text>
    <text class="display-line" x="76" y="611" font-size="142" textLength="610" lengthAdjust="spacingAndGlyphs">difference</text>
    <text class="serif-line" x="208" y="681" font-size="96" textLength="397" lengthAdjust="spacingAndGlyphs">tomorrow</text>
  </svg>

  <section class="program-band">
    <h1 class="program-title">NRU- Masters of Accounting</h1>
  </section>

  <section class="rankings">
    <p class="rankings-label">Ranked amongst:</p>
    <div class="badge badge-college">
      <div class="badge-shape" role="img" aria-label="Best college 2023 listing badge"></div>
      <p class="badge-caption">Best Colleges-Meridian 2023</p>
    </div>
    <div class="badge badge-master">
      <div class="badge-shape" role="img" aria-label="Best master 2023 ranking badge"></div>
      <p class="badge-caption">Best Masters in Accounting<br>- Scholaris 2023</p>
    </div>
  </section>

  <section class="outcomes-band">
    <p class="outcomes-text">NRS graduates have gone on to work in various high-quality jobs in top firms,<br>earning impressive six-figure salaries as well as opening successful businesses.</p>
  </section>
</main>
</body>
</html>
```